Community-based social network needs a new landing page

We need a landing page for a local social network in Singapore called "LaneSharely.sg". It is a website that help neighbours to connect with each other for mutual benefits such as providing professional/non-professional services, sharing items, and neighbourly help, etc.

There is an existing website but we want to completely revamp it. It is most important that the new landing page communicates that the neighbourhood has skills and services for people to discover.

The final design of the landing page should be modern, and communicates a sense of community and vibrancy. As a matter of priority, more real estate should be accorded to the neighbours providing services elements.

We have drafted 2 reference sites that communicates the key ideas/user propositions for your easy reference:
http://tarvelqix7.example-sites.com/lanesharely
http://tarvelqix7.example-sites.com/lanesharely2

As long as the key ideas/user propositions are kept to, we are open to any design proposals. I.e. you do not have to follow the design layout of the reference sites

Target Market(s)

Our target market is primarily the Singapore community, includes all genders, education levels and occupations, aged between 17-45 years old.

In the file uploaded, you will find pictures of Singapore neighbourhoods and people of local ethnicities. Please use them, but you may arrange and add further filters to better enhance them

Industry/Entity Type

Real Estate

Requirements
Nice to have
• Landing page could be similar to that of www.gatherpondo.com, not just at the top, but also the way the other categories are presented at the bottom.

```html
<!DOCTYPE html>
<html lang="en">
<head>
<meta charset="utf-8">
<title>LaneSharely.sg – Find people living near you</title>
<link rel="stylesheet" href="https://fonts.googleapis.com/css2?family=Open+Sans:wght@300;400;600;700&display=swap">
<style>
:root{
  --white:#ffffff;
  --ink:#333333;
  --green:#7cbf2a;
  --red:#d42127;
  --blue:#3a6aa8;
  --pale:#e9ecef;
  --dark:#3a3a3a;
  --darker:#111111;
  --footer-text:#8f8f8f;
  --bubble:rgba(18,18,22,.8);
}
*{box-sizing:border-box;margin:0;padding:0}
html,body{width:811px;height:1200px;overflow:hidden}
body{font-family:"Open Sans",Arial,sans-serif;color:var(--ink);background:var(--white);position:relative}
.abs{position:absolute}

/* header */
.site-header{position:absolute;left:0;top:0;width:811px;height:64px;background:var(--white)}
.brand{left:68px;top:20px;display:flex;align-items:center;gap:7px;font-size:23px;font-weight:700;color:#444;letter-spacing:-.5px;line-height:28px}
.brand-dot{width:14px;height:14px;border-radius:50%;background:var(--red)}
.btn-top{top:24px;width:64px;height:19px;border-radius:2px;color:var(--white);font-size:10px;font-weight:600;text-align:center;line-height:19px}
.btn-signup{left:539px;background:linear-gradient(#8fd03b,#64a81c)}
.btn-login{left:610px;background:linear-gradient(#e8373c,#b9161b)}
.btn-social{left:680px;background:linear-gradient(#4d72bd,#2f4f93);padding-left:14px}
.btn-social::before{content:"";position:absolute;left:5px;top:4px;width:11px;height:11px;background:rgba(255,255,255,.85);border-radius:1px}

/* hero: evening city tones as layered soft gradients */
.hero{position:absolute;left:0;top:64px;width:811px;height:370px;overflow:hidden;
  background:
    radial-gradient(ellipse 120px 90px at 600px 150px,rgba(255,196,90,.55),transparent 70%),
    radial-gradient(ellipse 140px 70px at 330px 200px,rgba(255,214,130,.45),transparent 70%),
    radial-gradient(ellipse 110px 80px at 760px 200px,rgba(255,170,70,.5),transparent 70%),
    radial-gradient(ellipse 160px 60px at 240px 300px,rgba(255,190,110,.4),transparent 70%),
    radial-gradient(ellipse 90px 110px at 40px 130px,rgba(240,200,140,.35),transparent 70%),
    radial-gradient(ellipse 200px 50px at 560px 330px,rgba(60,80,140,.55),transparent 70%),
    linear-gradient(180deg,#1f3f9a 0%,#2f4f9e 12%,#465a82 30%,#8a7356 48%,#a5794a 60%,#7c4c36 76%,#5a3a33 90%,#3a2c2e 100%)}
.avatar{border-radius:50%;border:3px solid rgba(255,255,255,.85);width:128px;height:128px;box-shadow:0 2px 8px rgba(0,0,0,.4)}
.avatar-one{left:72px;top:42px;background:radial-gradient(circle at 55% 60%,#e8c0a0 0%,#c99a7a 35%,#8a5e44 60%,#f1ece4 62%,#d8cfc2 100%)}
.avatar-two{left:612px;top:196px;background:radial-gradient(circle at 50% 55%,#eab898 0%,#c47a54 40%,#9c4a2a 65%,#d8d4cc 100%)}
.bubble{background:var(--bubble);color:var(--white);font-size:11.3px;line-height:17px}
.bubble-one{left:218px;top:86px;width:334px;height:42px;padding:4px 12px 0 24px}
.bubble-one::before{content:"";position:absolute;left:-14px;top:10px;border:11px solid transparent;border-right:14px solid var(--bubble);border-left:0}
.bubble-two{left:264px;top:256px;width:330px;height:43px;line-height:43px;padding-left:12px}
.bubble-two::after{content:"";position:absolute;right:-14px;top:11px;border:11px solid transparent;border-left:14px solid var(--bubble);border-right:0}

/* features */
.features{position:absolute;left:0;top:434px;width:811px;height:321px;background:linear-gradient(#eef0f3,#e4e7eb)}
.features-title{position:absolute;top:20px;width:811px;text-align:center;font-size:19px;font-weight:300;color:#555}
.feature{position:absolute;top:70px;width:180px;text-align:center}
.feature svg{display:block;margin:0 auto}
.feature-label{margin-top:20px;font-size:16.5px;font-weight:600;text-shadow:0 1px 0 #fff}
.f-pro{left:54px}.f-pro .feature-label{color:var(--blue)}
.f-non{left:317px}.f-non .feature-label{color:var(--red)}
.f-share{left:578px}.f-share .feature-label{color:#3a3a3a}

.band{position:absolute;left:0;top:755px;width:811px;height:15px;background:var(--red)}

/* activity */
.activity{position:absolute;left:0;top:770px;width:811px;height:212px;background:var(--dark);color:var(--white)}
.col-title{position:absolute;top:14px;font-size:11.5px;font-weight:600}
.posts{position:absolute;left:68px;top:41px;list-style:none}
.posts li{height:21.3px;font-size:8.5px;color:#aaa;display:flex;align-items:center;gap:9px}
.posts i{display:block;width:11px;height:8px;background:#777;border-radius:2px}
.posts i.round{border-radius:50%;width:10px}
.members{position:absolute;left:305px;top:44px;display:grid;grid-template-columns:repeat(4,46px);gap:7px 5px}
.members span{width:46px;height:46px;border:1px solid #555}
.btn-grey{position:absolute;background:#6b6b6b;color:var(--white);font-size:11px;text-align:center}
.join{left:305px;top:152px;width:73px;height:24px;line-height:24px}
.news-copy{position:absolute;left:552px;top:43px;width:195px;font-size:8.5px;line-height:14px;color:#999;font-weight:300}
.news-input{position:absolute;left:553px;top:76px;width:165px;height:24px;background:var(--white);font-size:8px;color:#999;padding:7px 11px}
.news-btn{left:553px;top:111px;width:74px;height:24px;line-height:24px}

/* footer */
.site-footer{position:absolute;left:0;top:982px;width:811px;height:218px;background:var(--darker);color:var(--white)}
.foot-title{position:absolute;font-size:11.5px;font-weight:600}
.foot-copy{position:absolute;font-size:8.3px;line-height:14px;color:var(--footer-text)}
.share-box{position:absolute;left:415px;top:37px;width:328px;height:51px;background:#e9e9e9;border-radius:3px}
.count{position:absolute;top:5px;width:36px;height:22px;background:var(--white);border:1px solid #ccc;font-size:10px;color:#333;text-align:center;line-height:20px}
.mini{position:absolute;top:31px;height:13px;background:#f5f5f5;border:1px solid #bbb;border-radius:2px;font-size:7px;font-weight:700;color:#345;padding:0 4px;line-height:11px}
.like-note{position:absolute;left:90px;top:7px;font-size:7px;color:#333;display:flex;align-items:center;gap:4px}
.like-note b{background:#dfe4ef;border:1px solid #aab;font-size:7px;padding:0 3px;color:#3b5ea8}
.divider{position:absolute;left:68px;top:118px;width:675px;height:1px;background:#2e2e2e}
.links{position:absolute;top:153px;list-style:none;font-size:8.5px;font-weight:700;color:#888;letter-spacing:.3px;line-height:12px}
</style>
</head>
<body>

<header class="site-header">
  <div class="abs brand"><span class="brand-dot"></span>LaneSharely.sg</div>
  <div class="abs btn-top btn-signup">Sign Up</div>
  <div class="abs btn-top btn-login">Login</div>
  <div class="abs btn-top btn-social">Login</div>
</header>

<section class="hero" role="img" aria-label="Evening skyline of a Singapore neighbourhood with lit towers and shophouse rooftops">
  <div class="abs avatar avatar-one" role="img" aria-label="Portrait photo of neighbour Rina"></div>
  <p class="abs bubble bubble-one">Rina is offering professional home-call beauty services at low rates</p>
  <p class="abs bubble bubble-two">Mei is offering hourly housekeeping at $13 per hour</p>
  <div class="abs avatar avatar-two" role="img" aria-label="Portrait photo of neighbour Mei"></div>
</section>

<section class="features">
  <h2 class="features-title">Find people living near you for useful things &amp; neighbourly help</h2>

  <div class="feature f-pro">
    <svg width="150" height="176" viewBox="0 0 150 176">
      <polygon points="75,6 148,48 148,134 75,176 2,134 2,48" fill="#d7dbe0"/>
      <polygon points="75,0 148,42 148,128 75,170 2,128 2,42" fill="#f6f7f9" stroke="#e1e4e8"/>
      <path d="M58 118 v-13 c-10-7-16-19-14-32 c3-20 19-31 36-31 c18 0 32 13 32 31 l8 13 h-8 v10 c0 6-4 8-10 8 h-8 v14 z" fill="#3a6aa8"/>
      <circle cx="82" cy="70" r="19" fill="#f6f7f9"/>
      <g stroke="#3a6aa8" stroke-width="5" stroke-linecap="round">
        <line x1="73" y1="61" x2="91" y2="79"/>
        <line x1="91" y1="61" x2="73" y2="79"/>
      </g>
    </svg>
    <p class="feature-label">Professional Services</p>
  </div>

  <div class="feature f-non">
    <svg width="150" height="176" viewBox="0 0 150 176">
      <polygon points="75,6 148,48 148,134 75,176 2,134 2,48" fill="#d7dbe0"/>
      <polygon points="75,0 148,42 148,128 75,170 2,128 2,42" fill="#f6f7f9" stroke="#e1e4e8"/>
      <line x1="38" y1="52" x2="56" y2="86" stroke="#d42127" stroke-width="4" stroke-linecap="round"/>
      <path d="M54 84 l18 14 v-14 c0-6 4-10 10-10 h10 c8 0 14 6 16 14 l6 18 h-22 v14 h-16 v-18 l-24-14 z" fill="#d42127"/>
      <circle cx="88" cy="60" r="9" fill="#d42127"/>
      <rect x="80" y="96" width="14" height="20" fill="#f6f7f9"/>
    </svg>
    <p class="feature-label">Non-professionals</p>
  </div>

  <div class="feature f-share">
    <svg width="150" height="176" viewBox="0 0 150 176">
      <polygon points="75,6 148,48 148,134 75,176 2,134 2,48" fill="#d7dbe0"/>
      <polygon points="75,0 148,42 148,128 75,170 2,128 2,42" fill="#f6f7f9" stroke="#e1e4e8"/>
      <g fill="#f6f7f9" stroke="#2b2b2b" stroke-width="5" stroke-linejoin="round">
        <path d="M70 78 h26 a16 16 0 0 1 16 16 v6 a16 16 0 0 1 -16 16 h-2 l2 14 -14 -14 h-12 a16 16 0 0 1 -16 -16 v-6 a16 16 0 0 1 16 -16z"/>
        <path d="M56 56 h30 a16 16 0 0 1 16 16 v6 a16 16 0 0 1 -16 16 h-18 l-12 12 2 -12 a16 16 0 0 1 -18 -16 v-6 a16 16 0 0 1 16 -16z"/>
      </g>
    </svg>
    <p class="feature-label">Share &amp; Help</p>
  </div>
</section>

<div class="band"></div>

<section class="activity">
  <h3 class="col-title" style="left:68px">Lates Posts</h3>
  <ul class="posts">
    <li><i class="round"></i>Sufen Tay has shared Measuring Tape</li>
    <li><i></i>Sufen Tay has shared Measuring Tape</li>
    <li><i class="round"></i>Sufen Tay has shared Novels</li>
    <li><i class="round"></i>Sufen Tay has shared Children Books</li>
    <li><i></i>Sufen Tay has shared Self Help Books</li>
    <li><i class="round"></i>Sufen Tay has shared Measuring Tape</li>
    <li><i></i>Sufen Tay has shared Novels</li>
  </ul>

  <h3 class="col-title" style="left:303px">Latest Members</h3>
  <div class="members">
    <span role="img" aria-label="Member photo" style="background:linear-gradient(135deg,#8a7ea0,#c9a48e)"></span>
    <span role="img" aria-label="Member photo" style="background:linear-gradient(135deg,#6a4a3e,#c08a6a)"></span>
    <span role="img" aria-label="Member photo" style="background:linear-gradient(135deg,#c0604a,#8a2e24)"></span>
    <span role="img" aria-label="Member photo" style="background:linear-gradient(135deg,#e0c8b8,#a88878)"></span>
    <span role="img" aria-label="Member photo" style="background:linear-gradient(135deg,#c8403a,#6a8a3a)"></span>
    <span role="img" aria-label="Member photo" style="background:linear-gradient(135deg,#2e2430,#6a5060)"></span>
    <span role="img" aria-label="Member photo" style="background:linear-gradient(135deg,#b08a5a,#5a3a2a)"></span>
    <span role="img" aria-label="Member photo" style="background:linear-gradient(135deg,#c8c0ba,#6a5a58)"></span>
  </div>
  <div class="btn-grey join">Join for free</div>

  <h3 class="col-title" style="left:552px">Subscribe Newsletter</h3>
  <p class="news-copy">Integer eu libero sit amet nisl vestibulum semp edfs pdisioolpr.</p>
  <div class="news-input">Your Email...</div>
  <div class="btn-grey news-btn">Sign Up</div>
</section>

<footer class="site-footer">
  <h3 class="foot-title" style="left:68px;top:16px">Media Mentions</h3>
  <p class="foot-copy" style="left:68px;top:33px;width:230px">LaneSharely.sg is an initiative supported by CNCL.</p>
  <p class="foot-copy" style="left:68px;top:51px;width:230px">“LaneSharely.sg fills a critical gap, by providing a mechanism for neighbours to communicate with each other their resources and their willingness to help.”<br>- CEO Darren Koh of CNCL</p>

  <h3 class="foot-title" style="left:413px;top:16px">If you found LaneSharely.sg useful, tell your friends about it!</h3>
  <div class="share-box">
    <div class="count" style="left:6px">21</div>
    <div class="count" style="left:50px;width:32px">11</div>
    <div class="mini" style="left:6px">Post</div>
    <div class="mini" style="left:50px">Share</div>
    <div class="like-note"><b>Like</b>516 people like this. Be the first of your friends.</div>
  </div>

  <div class="divider"></div>

  <h3 class="foot-title" style="left:68px;top:132px">Want to know more?</h3>
  <ul class="links" style="left:68px"><li>About us</li><li>FAQ</li></ul>
  <h3 class="foot-title" style="left:218px;top:132px">Using LaneSharely</h3>
  <ul class="links" style="left:218px"><li>Terms of Use</li><li>Privacy Policy</li></ul>
  <h3 class="foot-title" style="left:386px;top:132px">Get in touch</h3>
  <ul class="links" style="left:386px"><li>Contact us</li><li>Circlebook</li></ul>
  <h3 class="foot-title" style="left:500px;top:132px">© Kerbview Pte Ltd 2013</h3>
  <p class="foot-copy" style="left:500px;top:148px;width:245px">LaneSharely.sg is a website of Kerbview Pte Ltd. We help you pool together physical items, efforts, and purchasing power with your favourite neighbours so that you can save money, free up space at home, be eco-friendly.</p>
</footer>

</body>
</html>
```